Business card design for new, innovative company - BluePlinth

We are a new company looking for a business card design that is fun, different and quirky. Must use corporate colour green - CMYK C:55, M:0, Y:100, K:0, and corporate colour grey - C:0, M:0, Y: 0, K:70.

We have developed the first real time data application, in which people are able to profile the data of their existing customers in order to pull out more good fit clients to direct their marketing activities at.

Industry/Entity Type

Marketing

Requirements
Must have
• Logo, name, title, telephone number, fax number, email, website, address

```html
<!DOCTYPE html>
<html lang="en">
<head>
<meta charset="utf-8">
<title>BluePlinth business card</title>
<link rel="stylesheet" href="https://fonts.googleapis.com/css2?family=Open+Sans:wght@400;600;700&family=Raleway:wght@400&display=swap">
<style>
  :root {
    --sky-top: #aee8ec;
    --sky-bottom: #c3f1f4;
    --brand-green: #7cc242;
    --brand-grey: #6d6e71;
    --ink: #333333;
    --card-white: #fbfbfb;
    --page: #ffffff;
    --photo-light: #d9c3ad;
    --photo-mid: #a37a5a;
    --photo-dark: #5b4636;
  }
  * { margin: 0; padding: 0; box-sizing: border-box; }
  html, body { width: 1200px; height: 818px; overflow: hidden; background: var(--page); }
  body { position: relative; font-family: "Open Sans", Arial, sans-serif; color: var(--ink); }

  .card {
    position: absolute;
    width: 515px; height: 310px;
    background: var(--card-white);
    box-shadow: 0 6px 14px rgba(0,0,0,0.18);
    overflow: hidden;
  }
  .card--front-a { left: 51px;  top: 68px; }
  .card--back-a  { left: 622px; top: 70px; }
  .card--front-b { left: 49px;  top: 447px; }
  .card--back-b  { left: 620px; top: 447px; }

  .sky {
    position: absolute; left: 0; top: 0; width: 100%; height: 182px;
    background: linear-gradient(180deg, var(--sky-top), var(--sky-bottom));
  }
  .stripe {
    position: absolute; left: 0; top: 182px; width: 100%; height: 9px;
    background: var(--brand-green);
  }
  .stripe--web {
    top: 181px; height: 22px;
    color: #fff; font-weight: 700; font-size: 15px; line-height: 22px; text-align: center;
  }

  .hero-photo {
    position: absolute; left: 164px; top: 12px; width: 186px; height: 170px;
    background:
      linear-gradient(90deg, #ffffff 0 54%, transparent 54%),
      linear-gradient(180deg, var(--photo-light), var(--photo-mid) 60%, var(--photo-dark));
    border-radius: 40px 40px 0 0;
  }
  .card--front-b .hero-photo { left: 171px; top: 13px; height: 168px; }

  .wordmark {
    position: absolute; left: 0; width: 100%; text-align: center;
    font-weight: 700; font-size: 60px; letter-spacing: -2px;
    color: var(--brand-green);
  }
  .card--front-a .wordmark { top: 206px; }
  .card--front-b .wordmark { top: 218px; }

  .brand-name {
    position: absolute; left: 30px; top: 70px;
    font-weight: 700; font-size: 24px; color: var(--brand-grey);
  }
  .card--back-b .brand-name { left: 42px; top: 90px; }

  .info-line {
    position: absolute; display: flex; align-items: center; gap: 6px;
    font-family: "Raleway", "Open Sans", sans-serif; font-size: 16px; color: var(--ink);
  }
  .info-line svg { width: 16px; height: 16px; flex: none; }
  .web-line { left: 164px; top: 76px; font-size: 18px; }
  .address-block {
    position: absolute; left: 190px; top: 106px;
    font-family: "Raleway", "Open Sans", sans-serif; font-size: 16px; line-height: 22px;
  }
  .address-block .pin { position: absolute; left: -24px; top: 3px; width: 16px; height: 16px; }
  .card--back-b .address-block { left: 188px; top: 97px; line-height: 25px; }

  .person-name {
    position: absolute; left: 46px; top: 210px;
    font-weight: 700; font-size: 15px; color: var(--ink);
  }
  .card--back-b .person-name { top: 211px; }

  .contact-list { position: absolute; left: 186px; top: 211px; list-style: none; }
  .card--back-b .contact-list { top: 214px; }
  .contact-list li {
    display: flex; align-items: center; gap: 7px; height: 22.5px;
    font-family: "Raleway", "Open Sans", sans-serif; font-size: 15.5px;
  }
  .contact-list svg { width: 15px; height: 15px; flex: none; }
</style>
</head>
<body>

<section class="card card--front-a">
  <div class="sky"></div>
  <div class="hero-photo" role="img" aria-label="Photo of a smiling young woman holding a clipboard checklist"></div>
  <div class="stripe"></div>
  <div class="wordmark">BluePlinth</div>
</section>

<section class="card card--back-a">
  <div class="sky"></div>
  <div class="brand-name">BluePlinth</div>
  <div class="info-line web-line">
    <svg viewBox="0 0 16 16" fill="none" stroke="#333" stroke-width="1.3"><circle cx="8" cy="8" r="6.5"/><ellipse cx="8" cy="8" rx="3" ry="6.5"/><path d="M1.5 8h13M2.5 4.8h11M2.5 11.2h11"/></svg>
    <span>www.blueplinth.com</span>
  </div>
  <div class="address-block">
    <svg class="pin" viewBox="0 0 16 16" fill="#333"><path d="M8 1 1 7h2v8h4v-5h2v5h4V7h2z"/></svg>
    8 Orchard Lane, Ely,<br>Cambridgeshire, CB7 4QT
  </div>
  <div class="stripe"></div>
  <div class="person-name">Clara Bennett</div>
  <ul class="contact-list">
    <li><svg viewBox="0 0 16 16" fill="none" stroke="var(--brand-green)" stroke-width="1.5"><rect x="4" y="1" width="8" height="14" rx="1.5"/><path d="M4 12h8"/></svg>07700900418</li>
    <li><svg viewBox="0 0 16 16" fill="var(--brand-green)"><path d="M4 1l3 3-2 2c1 2 3 4 5 5l2-2 3 3-2 3C7 15 1 9 1 3z"/></svg>01632 960482</li>
    <li><svg viewBox="0 0 16 16" fill="none" stroke="var(--brand-green)" stroke-width="1.4"><rect x="1" y="3" width="14" height="10"/><path d="M1 3l7 6 7-6"/></svg>clara.bennett@northgatemedia.com</li>
  </ul>
</section>

<section class="card card--front-b">
  <div class="sky"></div>
  <div class="hero-photo" role="img" aria-label="Photo of a smiling young woman holding a clipboard checklist"></div>
  <div class="stripe stripe--web">www.blueplinth.com</div>
  <div class="wordmark">BluePlinth</div>
</section>

<section class="card card--back-b">
  <div class="sky"></div>
  <div class="brand-name">BluePlinth</div>
  <div class="address-block">8 Orchard Lane, Ely,<br>Cambridgeshire, CB7 4QT</div>
  <div class="stripe stripe--web">www.blueplinth.com</div>
  <div class="person-name">Clara Bennett</div>
  <ul class="contact-list">
    <li><svg viewBox="0 0 16 16" fill="none" stroke="var(--brand-green)" stroke-width="1.5"><rect x="4" y="1" width="8" height="14" rx="1.5"/><path d="M4 12h8"/></svg>07700900418</li>
    <li><svg viewBox="0 0 16 16" fill="var(--brand-green)"><path d="M4 1l3 3-2 2c1 2 3 4 5 5l2-2 3 3-2 3C7 15 1 9 1 3z"/></svg>01632 960482</li>
    <li><svg viewBox="0 0 16 16" fill="none" stroke="var(--brand-green)" stroke-width="1.4"><rect x="1" y="3" width="14" height="10"/><path d="M1 3l7 6 7-6"/></svg>clara.bennett@northgatemedia.com</li>
  </ul>
</section>

</body>
</html>
```